Display Ad for Local Publication

We have never advertised before but now I would like to have an ad running in our local, community magazine. Our business is Brackwater Mini Storage located in Port Ludlow, WA. PL is a small community (+/-2,500 people located across the Puget Sound from Seattle. The monthly magazine, The Herald, covers all kinds of local news and activities and carries a number of ads from local businesses. Our is the only mini storage in Port Ludlow. We have enclosed storage units of various sizes and outdoor parking spaces for boats, trailers and RVs. I am enclosing a business card and the size requirements for Herald advertisements. I want to develop a 1/8 page ad.

```html
<!DOCTYPE html>
<html lang="en">
<head>
<meta charset="utf-8">
<title>Brackwater Mini Storage – Display Ad</title>
<link href="https://fonts.googleapis.com/css2?family=Anton&family=Oswald:wght@400&family=Open+Sans:ital,wght@1,700&display=swap" rel="stylesheet">
<style>
  :root {
    --brand-green: #55bb5a;
    --photo-green: #8fd27f;
    --photo-light: #d9e6d4;
    --ink: #000000;
    --paper: #ffffff;
    --backdrop: #c0c0c0;
  }
  html, body {
    margin: 0;
    width: 1200px;
    height: 791px;
    overflow: hidden;
    background: var(--backdrop);
  }
  .ad {
    position: absolute;
    left: 0;
    top: 23px;
    width: 1200px;
    height: 745px;
    background: var(--ink);
    overflow: hidden;
  }
  .ad__top-band {
    position: absolute;
    left: 0; top: 0;
    width: 1200px; height: 371px;
    background: var(--brand-green);
  }
  .ad__photo {
    position: absolute;
    left: 500px; top: 0;
    width: 700px; height: 308px;
    background:
      linear-gradient(90deg, var(--brand-green) 0%, rgba(85,187,90,0) 30%),
      linear-gradient(90deg, var(--photo-green) 0%, #7cc46c 40%, #b7c9ad 62%, var(--photo-light) 80%, #9fd68d 100%);
  }
  .ad__headline {
    position: absolute;
    left: 56px; top: 58px;
    margin: 0;
    font-family: "Anton", Impact, sans-serif;
    font-weight: 400;
    font-size: 101px;
    line-height: 98px;
    letter-spacing: -1px;
    color: var(--ink);
    text-transform: uppercase;
  }
  .ad__services {
    position: absolute;
    left: 62px; top: 436px;
    margin: 0;
    font-family: "Oswald", "Arial Narrow", sans-serif;
    font-size: 44px;
    line-height: 56px;
    letter-spacing: -0.5px;
    color: var(--paper);
  }
  .ad__name-pill {
    position: absolute;
    left: 430px; top: 308px;
    width: 770px; height: 298px;
    background: var(--paper);
    border-radius: 150px 0 0 150px;
  }
  .ad__name-pill-inner {
    position: absolute;
    left: 18px; top: 18px;
    width: 752px; height: 262px;
    background: var(--brand-green);
    border-radius: 132px 0 0 132px;
    display: flex;
    align-items: center;
    justify-content: center;
  }
  .ad__business-name {
    margin: 0 0 0 60px;
    font-family: "Open Sans", Arial, sans-serif;
    font-style: italic;
    font-weight: 700;
    font-size: 74px;
    line-height: 90px;
    text-align: center;
    color: var(--paper);
    letter-spacing: -1px;
  }
  .ad__cta,
  .ad__phone {
    position: absolute;
    top: 628px;
    margin: 0;
    font-family: "Open Sans", Arial, sans-serif;
    font-style: italic;
    font-weight: 700;
    font-size: 62px;
    line-height: 80px;
    letter-spacing: -1px;
  }
  .ad__cta { left: 54px; color: var(--brand-green); }
  .ad__phone { right: 70px; color: var(--paper); }
</style>
</head>
<body>
  <article class="ad">
    <div class="ad__top-band"></div>
    <div class="ad__photo" role="img" aria-label="Photo: two people checking cardboard boxes in a hallway of green storage unit doors"></div>

    <h1 class="ad__headline">Your only<br>storage in Port<br>Ludlow.</h1>

    <p class="ad__services">Units &amp; Outdoor<br>Parking for Boats,<br>RVs &amp; Trailers.</p>

    <div class="ad__name-pill">
      <div class="ad__name-pill-inner">
        <p class="ad__business-name">Brackwater<br>Mini Storage</p>
      </div>
    </div>

    <p class="ad__cta">CALL US TODAY!</p>
    <p class="ad__phone">360-555-0148</p>
  </article>
</body>
</html>
```